Company Intro Banner for new company website

Harrowgate Components, Inc is a resistor manufacturer and a well known brand named HCI. We are creating a new customer facing web site that needs a well designed professional introduction in the form of a banner. There are several files attached to this project request. The Intro Banner Design Request.pdf file describes the project in full details.

Target Market(s)

Our primary audience are Electronic Design Engineers, Electronics Manufacturers (like Pindle, Corvanta, Brix, etc)

Industry/Entity Type

Electronics

Requirements
Must have
• Please refer to the narrative attached to this project.
Should not have
• The banner/tile should not over power our new web site design. It should augment the site and specifically tell folks that visit our new site they have come to HCI Harrowgate Components.

```html
<!DOCTYPE html>
<html lang="en">
<head>
<meta charset="utf-8">
<title>HCI Harrowgate Components — Intro Banner</title>
<link href="https://fonts.googleapis.com/css2?family=Arimo:wght@400;700&display=swap" rel="stylesheet">
<style>
  :root {
    --paper: #fbfaf8;
    --paper-edge: #e7e5e2;
    --maroon-deep: #5c0705;
    --maroon: #6b1012;
    --maroon-band: #600a08;
    --brand: #6a1215;
    --tagline: #5a0b0b;
    --white: #ffffff;
    --shadow: #d9d8d6;
  }
  * { margin: 0; padding: 0; box-sizing: border-box; }
  html, body {
    width: 1200px; height: 338px; overflow: hidden; background: var(--white);
  }
  .banner {
    position: relative; width: 1200px; height: 338px;
    font-family: "Arimo", Arial, sans-serif;
  }
  .banner__shadow {
    position: absolute; left: 0; top: 300px; width: 1200px; height: 30px;
    background: radial-gradient(ellipse at 50% 0%, rgba(0,0,0,0.22), rgba(0,0,0,0) 70%);
  }
  .banner__field {
    position: absolute; left: 0; top: 0; width: 1200px; height: 310px;
  }
  .brand {
    position: absolute; left: 50px; top: 88px; color: var(--brand);
  }
  .brand__name {
    font-size: 96px; font-weight: 700; line-height: 1; letter-spacing: -2px;
  }
  .brand__legal {
    margin-top: 16px; font-size: 16px; font-weight: 400; letter-spacing: 0.3px;
    text-transform: uppercase;
  }
  .tagline {
    position: absolute; left: 359px; top: 102px; width: 460px;
    font-size: 26px; line-height: 33px; color: var(--tagline);
  }
  .values {
    position: absolute; left: 1048px; top: 80px; list-style: none;
    color: var(--white); font-size: 18px;
  }
  .values li {
    display: flex; align-items: center; height: 24px; margin-bottom: 16px;
  }
  .values li:last-child { font-size: 20px; margin-top: 2px; }
  .values svg { margin-right: 12px; }
</style>
</head>
<body>
<div class="banner">
  <div class="banner__shadow"></div>
  <svg class="banner__field" width="1200" height="310" viewBox="0 0 1200 310">
    <defs>
      <radialGradient id="paper" cx="0.3" cy="0.45" r="0.75">
        <stop offset="0" stop-color="var(--paper)"/>
        <stop offset="0.6" stop-color="#f5f3f1"/>
        <stop offset="1" stop-color="var(--paper-edge)"/>
      </radialGradient>
    </defs>
    <rect width="1200" height="310" fill="var(--maroon)"/>
    <polygon points="706,0 850,0 1044,155 850,310 706,310 900,155" fill="var(--maroon-deep)"/>
    <polygon points="0,0 706,0 900,155 706,310 0,310" fill="url(#paper)"/>
  </svg>

  <div class="brand">
    <div class="brand__name">HCI</div>
    <div class="brand__legal">Harrowgate Components, Inc.</div>
  </div>

  <p class="tagline">For passive components &amp; active services, contact the leader in Resistive Product Solutions.</p>

  <ul class="values">
    <li><svg width="8" height="10" viewBox="0 0 8 10"><polygon points="0,0 8,5 0,10" fill="#fff"/></svg>Flexibility</li>
    <li><svg width="8" height="10" viewBox="0 0 8 10"><polygon points="0,0 8,5 0,10" fill="#fff"/></svg>Service</li>
    <li><svg width="8" height="10" viewBox="0 0 8 10"><polygon points="0,0 8,5 0,10" fill="#fff"/></svg>Quality</li>
    <li><svg width="8" height="10" viewBox="0 0 8 10"><polygon points="0,0 8,5 0,10" fill="#fff"/></svg>Delivery</li>
  </ul>
</div>
</body>
</html>
```